Talbern Learning Recruitment Business Cards

We need business cards designed for our growing recruitment business.
We have just launched our offices in Sydney Melbourne and have a well established business in Perth. We are a fun young firm that specialise in Early Years Education Recruitment.
Our vision mission values are below
Our Vision:
To be:
the single, nationally recognised leader in the Early Childhood Sector.
a multifaceted organisation with a network of expertly driven facilities in the Early Childhood Sector, acknowledged as an organisation of integrity, innovation, heart and community.

Our Mission:
To provide superior quality recruitment services and solutions to the Early Childhood sector.
We empower our candidates to succeed.
We engage in trusted partnerships with our clients.
We grow our business/network/community, with passion and integrity.

Our Values:

We… are REAL
think: CUSTOMER
find: SOLUTIONS
achieve: RESULTS
enjoy: WHAT WE DO

Our website is www.talbernlearning.com feel free to visit it for inspiration.
Name Felix Ormsby
Title National Director
1300 057 812
0462 315 706
felix@talbernstaffing.com
website www.talbernlearning.com

I have attached our current business cards and logo designs to view

Target Market(s)

Recruitment

Industry/Entity Type

Business

Contact Information for Business Card

Name Felix Ormsby
Title National Director
1300 057 812
0462 315 706

Font styles to use
Serif

Requirements
Must have
• Company Values and the cities we have offices in Perth | Sydney | Melbourne
Nice to have
• Our Vision on the card
• Our Vision:
• To be a nationally recognised leader in the Early Childhood Sector.
• A multifaceted organisation with a network of expertly driven facilities in the Early Childhood Sector, acknowledged as an organisation of integrity, innovation, heart and community.

```html
<!DOCTYPE html>
<html lang="en">
<head>
<meta charset="utf-8">
<title>Talbern Learning Recruitment – Business Cards</title>
<link href="https://fonts.googleapis.com/css2?family=Lora:wght@400;600;700&display=swap" rel="stylesheet">
<style>
  :root{
    --page:#e9ebeb;
    --navy:#0b3f6e;
    --blue:#1a6fae;
    --sky:#2b9fd9;
    --ink:#1d4f80;
    --text:#2f3a44;
    --grey:#555657;
    --white:#ffffff;
  }
  *{box-sizing:border-box;margin:0;padding:0}
  html,body{width:1200px;height:812px;overflow:hidden;background:var(--page)}
  body{position:relative;font-family:"Lora",Georgia,serif}

  .card{position:absolute;top:252px;width:540px;height:309px;overflow:hidden;
        box-shadow:0 6px 18px rgba(0,0,0,.18)}

  /* back side */
  .card-back{left:30px;background:radial-gradient(circle at 50% 42%,var(--sky) 0%,var(--blue) 40%,var(--navy) 88%)}
  .back-ring{position:absolute;left:205px;top:56px;width:130px;height:130px;border:3px solid var(--white);
        border-radius:50%;display:flex;flex-direction:column;align-items:center;justify-content:center;
        color:var(--white);font-weight:600;font-size:15px;letter-spacing:1px;line-height:1.25;text-align:center}
  .social{position:absolute;left:308px;top:198px;display:flex;gap:6px}
  .social span{width:24px;height:24px;border-radius:50%;background:var(--white)}
  .values{position:absolute;left:0;right:0;bottom:26px;text-align:center;color:var(--white);
        font-size:10px;letter-spacing:.3px;white-space:nowrap}
  .values b{font-weight:700}
  .values i{font-style:normal;margin:0 5px;opacity:.7}

  /* front side */
  .card-front{left:630px;background:var(--white)}
  .brand{position:absolute;left:34px;top:92px;width:260px;height:120px}
  .brand-circle{position:absolute;left:0;top:0;width:104px;height:104px;border-radius:50%;
        border:3px solid var(--blue)}
  .brand-name{position:absolute;left:112px;top:22px;font-weight:600;color:var(--ink);
        font-size:20px;letter-spacing:1px;line-height:1}
  .brand-sub{position:absolute;left:112px;top:46px;width:112px;text-align:right;font-weight:600;
        color:var(--ink);font-size:7.5px;letter-spacing:.6px}
  .tagline{position:absolute;left:24px;top:112px;font-weight:600;font-size:10px;color:var(--ink);white-space:nowrap}
  .tagline em{font-style:normal;color:var(--sky)}

  .contact{position:absolute;left:300px;top:48px}
  .person-name{font-weight:700;font-size:19px;color:var(--ink);letter-spacing:.5px}
  .person-title{font-weight:600;font-size:11px;color:var(--text);margin:2px 0 8px}
  .contact ul{list-style:none}
  .contact li{display:flex;align-items:center;gap:8px;font-size:11.5px;color:var(--text);line-height:18px;white-space:nowrap}
  .contact svg{width:11px;height:11px;fill:var(--ink);flex:none}

  .band{position:absolute;left:0;bottom:0;width:100%;height:46px;display:flex}
  .band-cities{flex:0 0 76%;background:linear-gradient(90deg,var(--navy),var(--blue) 60%,var(--sky));
        color:var(--white);font-size:15px;display:flex;align-items:center;padding-left:22px;letter-spacing:.3px}
  .band-cities b{font-weight:400;margin:0 7px;font-size:10px}
  .band-end{flex:1;background:var(--grey);position:relative}
  .band-dot{position:absolute;left:-14px;top:9px;width:28px;height:28px;border-radius:50%;
        background:var(--white);border:2px solid var(--blue)}
</style>
</head>
<body>

  <section class="card card-back" aria-label="Card back">
    <div class="back-ring"><span>TALBERN</span><span>LEARNING</span></div>
    <div class="social" aria-label="Social links">
      <span></span><span></span><span></span><span></span>
    </div>
    <p class="values">We are <b>REAL</b><i>•</i>think: <b>CUSTOMER</b><i>•</i>find: <b>SOLUTIONS</b><i>•</i>achieve: <b>RESULTS</b><i>•</i>enjoy: <b>WHAT WE DO</b></p>
  </section>

  <section class="card card-front" aria-label="Card front">
    <div class="brand">
      <div class="brand-circle"></div>
      <div class="brand-name">TALBERN</div>
      <div class="brand-sub">LEARNING</div>
      <div class="tagline">Bringing quality <em>to education recruitment</em></div>
    </div>

    <div class="contact">
      <div class="person-name">FELIX ORMSBY</div>
      <div class="person-title">National Director</div>
      <ul>
        <li><svg viewBox="0 0 24 24"><path d="M6.6 10.8a15 15 0 0 0 6.6 6.6l2.2-2.2c.3-.3.7-.4 1-.2 1.1.4 2.3.6 3.6.6.6 0 1 .4 1 1V20c0 .6-.4 1-1 1A17 17 0 0 1 3 4c0-.6.4-1 1-1h3.5c.6 0 1 .4 1 1 0 1.3.2 2.5.6 3.6.1.3 0 .7-.2 1z"/></svg>1300 057 812</li>
        <li><svg viewBox="0 0 24 24"><path d="M7 1h10a2 2 0 0 1 2 2v18a2 2 0 0 1-2 2H7a2 2 0 0 1-2-2V3a2 2 0 0 1 2-2zm0 3v14h10V4zm5 15.5a1.2 1.2 0 1 0 0 2.4 1.2 1.2 0 0 0 0-2.4z"/></svg>0462 315 706</li>
        <li><svg viewBox="0 0 24 24"><path d="M2 5h20v14H2zm2 2v.5l8 5 8-5V7zm0 3v7h16v-7l-8 5z"/></svg>felix@talbernstaffing.com</li>
        <li><svg viewBox="0 0 24 24"><path d="M12 2a10 10 0 1 0 0 20 10 10 0 0 0 0-20zm0 2c1 1.3 1.8 3 2.2 5H9.8c.4-2 1.2-3.7 2.2-5zM4.3 14a8 8 0 0 1 0-4h3.4a16 16 0 0 0 0 4zm5.5 1h4.4c-.4 2-1.2 3.7-2.2 5-1-1.3-1.8-3-2.2-5zm6.5-1a16 16 0 0 0 0-4h3.4a8 8 0 0 1 0 4z"/></svg>www.talbernlearning.com</li>
      </ul>
    </div>

    <div class="band">
      <div class="band-cities">Perth<b>●</b>Sydney<b>●</b>Melbourne</div>
      <div class="band-end"><span class="band-dot"></span></div>
    </div>
  </section>

</body>
</html>
```